Korvane Sky Works, LLC - Business Card

I currently have a drone business that specializes in aerial photography, thermal image inspections, deer recovery, search and rescue, custom agricultural applications. i will attach my current business card as well as some logos to incorporate for a new up to date business card
Updates

Designs look the same

Sick

Target Market(s)

farmers, hunters

Contact Information for Business Card

name address phone number (as existing card i attached)

Requirements
Must have
• im good with existing business card, but would like an agricultural twist

```html
<!DOCTYPE html>
<html lang="en">
<head>
<meta charset="utf-8">
<title>Korvane Sky Works, LLC – Business Cards</title>
<link href="https://fonts.googleapis.com/css2?family=Open+Sans:wght@400;700&family=Lato:wght@400&display=swap" rel="stylesheet">
<style>
  :root{
    --board:#8e8e8e;
    --green:#5a9a20;
    --red:#fe0000;
    --ink:#1f1f1f;
    --white:#ffffff;
    --label:#222222;
  }
  *{margin:0;padding:0;box-sizing:border-box}
  html,body{width:1200px;height:761px;overflow:hidden;background:var(--board)}
  .board{position:relative;width:1200px;height:761px;font-family:"Open Sans",Arial,sans-serif}
  .card{position:absolute;width:407px;height:232px;border-radius:15px;overflow:hidden;
        box-shadow:0 10px 18px rgba(0,0,0,.28)}
  .card--green-front{left:158px;top:124px;background:var(--green)}
  .card--red-front{left:636px;top:124px;background:var(--red)}
  .card--green-back{left:158px;top:406px;background:var(--ink)}
  .card--red-back{left:636px;top:406px;background:var(--ink)}
  .card__curve{position:absolute;inset:0;width:407px;height:232px}
  .contact{position:absolute;left:25px;top:48px;color:var(--white)}
  .contact__name{font-weight:700;font-size:19.5px;line-height:1;letter-spacing:.2px}
  .contact__title{font-size:11px;margin-top:3px}
  .contact__list{list-style:none;margin-top:10px;font-size:9.6px;line-height:14px}
  .contact__list li{position:relative;padding-left:16px}
  .contact__list li.gap{margin-top:4px}
  .contact__list svg{position:absolute;left:0;top:3px;width:8px;height:8px;fill:var(--white)}
  .brand{position:absolute;display:flex;flex-direction:column;align-items:center;justify-content:center;text-align:center}
  .brand__ring{border-radius:50%;display:flex;align-items:center;justify-content:center}
  .brand__name{font-family:"Open Sans",Arial,sans-serif;font-weight:700;letter-spacing:1px}
  .brand--green-front{left:255px;top:58px;width:116px;height:116px}
  .brand--green-front .brand__ring{width:108px;height:108px;border:3px solid var(--green)}
  .brand--green-front .brand__name{color:var(--green);font-size:16px}
  .brand--red-front{left:220px;top:80px;width:170px;height:70px;flex-direction:row;gap:8px}
  .brand__dot{width:18px;height:18px;border-radius:50%;background:var(--red)}
  .brand--red-front .brand__name{color:var(--red);font-size:22px}
  .brand--green-back{left:138px;top:40px;width:130px;height:130px}
  .brand--green-back .brand__ring{width:122px;height:122px;border:3px solid var(--green)}
  .brand--green-back .brand__name{color:var(--green);font-size:18px}
  .brand--red-back{left:90px;top:55px;width:227px;height:80px;flex-direction:row;gap:12px}
  .brand--red-back .brand__dot{width:26px;height:26px}
  .brand--red-back .brand__name{color:var(--red);font-size:34px}
  .services{position:absolute;left:0;right:0;top:186px;text-align:center;color:var(--white);
            font-family:"Lato",Arial,sans-serif;font-size:9.8px;line-height:14px}
  .services .sep{display:inline-block;width:4px;height:4px;border-radius:50%;margin:0 3px 2px}
  .card--green-back .sep{background:var(--green)}
  .card--red-back .sep{background:var(--red)}
  .label{position:absolute;top:669px;width:407px;text-align:center;font-family:"Lato",Arial,sans-serif;
         font-size:16px;letter-spacing:2px;color:var(--label)}
  .label--one{left:147px}
  .label--two{left:636px}
</style>
</head>
<body>
<main class="board">

  <section class="card card--green-front">
    <svg class="card__curve" viewBox="0 0 407 232" aria-hidden="true">
      <path d="M220 30 C170 95 180 165 248 232 L265 232 C200 168 190 100 235 18 Z" fill="var(--ink)"/>
      <path d="M247 0 C180 55 165 150 270 232 L407 232 L407 0 Z" fill="var(--white)"/>
    </svg>
    <div class="contact">
      <h1 class="contact__name">DALEN MARSH</h1>
      <p class="contact__title">Owner</p>
      <ul class="contact__list">
        <li><svg viewBox="0 0 10 10"><path d="M5 0a3.5 3.5 0 0 0-3.5 3.5C1.5 6 5 10 5 10s3.5-4 3.5-6.5A3.5 3.5 0 0 0 5 0zm0 5a1.4 1.4 0 1 1 0-2.8A1.4 1.4 0 0 1 5 5z"/></svg>Korvane Sky Works, LLC<br>214 W. Orchard St.<br>Delmont, OH 45990</li>
        <li class="gap"><svg viewBox="0 0 10 10"><path d="M2 0l2 2.5-1 1.2a6 6 0 0 0 3.3 3.3l1.2-1L10 8l-1.5 2C4 10 0 6 0 1.5z"/></svg>419-555-0142</li>
        <li><svg viewBox="0 0 10 10"><path d="M0 2h10v6H0zM0 2l5 3.5L10 2"/></svg>korvaneskyworks@mail.com</li>
        <li><svg viewBox="0 0 10 10"><circle cx="5" cy="5" r="4.5"/></svg>korvaneskyworks.com</li>
      </ul>
    </div>
    <div class="brand brand--green-front"><div class="brand__ring"><span class="brand__name">KORVANE</span></div></div>
  </section>

  <section class="card card--red-front">
    <svg class="card__curve" viewBox="0 0 407 232" aria-hidden="true">
      <path d="M220 30 C170 95 180 165 248 232 L265 232 C200 168 190 100 235 18 Z" fill="var(--ink)"/>
      <path d="M247 0 C180 55 165 150 270 232 L407 232 L407 0 Z" fill="var(--white)"/>
    </svg>
    <div class="contact">
      <h1 class="contact__name">DALEN MARSH</h1>
      <p class="contact__title">Owner</p>
      <ul class="contact__list">
        <li><svg viewBox="0 0 10 10"><path d="M5 0a3.5 3.5 0 0 0-3.5 3.5C1.5 6 5 10 5 10s3.5-4 3.5-6.5A3.5 3.5 0 0 0 5 0zm0 5a1.4 1.4 0 1 1 0-2.8A1.4 1.4 0 0 1 5 5z"/></svg>Korvane Sky Works, LLC<br>214 W. Orchard St.<br>Delmont, OH 45990</li>
        <li class="gap"><svg viewBox="0 0 10 10"><path d="M2 0l2 2.5-1 1.2a6 6 0 0 0 3.3 3.3l1.2-1L10 8l-1.5 2C4 10 0 6 0 1.5z"/></svg>419-555-0142</li>
        <li><svg viewBox="0 0 10 10"><path d="M0 2h10v6H0zM0 2l5 3.5L10 2"/></svg>korvaneskyworks@mail.com</li>
        <li><svg viewBox="0 0 10 10"><circle cx="5" cy="5" r="4.5"/></svg>korvaneskyworks.com</li>
      </ul>
    </div>
    <div class="brand brand--red-front"><span class="brand__dot"></span><span class="brand__name">KORVANE</span></div>
  </section>

  <section class="card card--green-back">
    <div class="brand brand--green-back"><div class="brand__ring"><span class="brand__name">KORVANE</span></div></div>
    <p class="services">THERMAL IMAGE INSPECTIONS<span class="sep"></span>DEER RECOVERY<br>SEARCH AND RESCUE<span class="sep"></span>REAL ESTATE PHOTOGRAPHY</p>
  </section>

  <section class="card card--red-back">
    <div class="brand brand--red-back"><span class="brand__dot"></span><span class="brand__name">KORVANE</span></div>
    <p class="services">THERMAL IMAGE INSPECTIONS<span class="sep"></span>DEER RECOVERY<br>SEARCH AND RESCUE<span class="sep"></span>REAL ESTATE PHOTOGRAPHY</p>
  </section>

  <p class="label label--one">FRONT &amp; BACK 01</p>
  <p class="label label--two">FRONT &amp; BACK 02</p>
</main>
</body>
</html>
```